Machinery buying in your area

We would like to let companies no that we are looking to buy machine tools and fabrication equipment in there area.

CNC Machinery, tool room machinery and fabrications equipment.

We pay more money on there trade in machines than the new dealers are offering .

Something quick to the point, fast to get there attention.

T & W Equipment Traders Inc, (248) 555-0143 Fax (248) 555-0197
sales@twequiptraders.example
www.twequiptraders.example, www.usedvalmorgrindersandpresses.example

Target Market(s)

shop guys, foreman, owner,Machinery buyers

Industry/Entity Type

Trade

Requirements
Nice to have
• Maybe this photo (crop some items out of the photos) on the card and the information on top of it?

Must catch there attention quick.

That I really do travel for a look, short and sweet

```html
<!DOCTYPE html>
<html lang="en">
<head>
<meta charset="utf-8">
<title>T &amp; W Equipment Traders – Postcard</title>
<link rel="stylesheet" href="https://fonts.googleapis.com/css2?family=Merriweather:wght@400;700&family=Merriweather+Sans:wght@400;700;800&display=swap">
<style>
  :root {
    --backdrop: #2b2b2b;
    --orange: #e8732a;
    --ink: #1c1c1c;
    --white: #ffffff;
    --steel-light: #ececec;
    --steel-mid: #c8c8c8;
    --steel-dark: #9c9c9c;
    --charcoal: #4a4a4a;
    --mesh-dark: #262626;
    --mesh-light: #5a5a5a;
  }
  * { margin: 0; padding: 0; box-sizing: border-box; }
  html, body { width: 748px; height: 1200px; overflow: hidden; background: var(--backdrop); }
  .canvas { position: relative; width: 748px; height: 1200px; }

  .card { position: absolute; overflow: hidden; }
  .card svg.card-art { position: absolute; inset: 0; }

  /* Front */
  .card-front { left: 37px; top: 40px; width: 670px; height: 518px; }
  .headline { position: absolute; left: 23px; font-family: "Merriweather Sans", sans-serif; font-weight: 800; line-height: 1; white-space: nowrap; }
  .headline-lead { top: 78px; font-size: 27px; color: var(--ink); }
  .headline-sub { top: 116px; font-size: 21px; color: var(--white); }
  .headline-small { top: 145px; font-size: 15.5px; color: var(--white); }
  .pitch { position: absolute; left: 23px; top: 190px; font-family: "Merriweather", serif; color: var(--ink); line-height: 1; }
  .pitch span { display: block; white-space: nowrap; }
  .pitch .pitch-open { font-size: 29px; color: var(--white); margin-bottom: 4px; }
  .pitch .pitch-line-1 { font-size: 16px; margin-bottom: 8px; }
  .pitch .pitch-line-2 { font-size: 17.5px; margin-bottom: 8px; }
  .pitch .pitch-line-3 { font-size: 19px; margin-bottom: 10px; }
  .pitch .pitch-line-4 { font-size: 19px; margin-bottom: 2px; }
  .pitch .pitch-close { font-size: 45px; color: var(--white); }
  .brand-name { position: absolute; left: 84px; top: 468px; font-family: "Merriweather Sans", sans-serif; font-weight: 700; font-size: 17px; color: var(--ink); white-space: nowrap; }

  /* Back */
  .card-back { left: 33px; top: 633px; width: 674px; height: 522px; background: var(--white); }
  .contact { position: absolute; right: 353px; top: 302px; text-align: right; color: var(--white); font-family: "Merriweather Sans", sans-serif; font-style: normal; }
  .contact-name { font-family: "Merriweather", serif; font-weight: 700; font-size: 17px; margin-bottom: 22px; white-space: nowrap; }
  .contact-list { list-style: none; font-size: 12px; line-height: 16px; white-space: nowrap; }
</style>
</head>
<body>
<main class="canvas">

  <section class="card card-front" aria-label="Postcard front">
    <svg class="card-art" width="670" height="518" viewBox="0 0 670 518">
      <defs>
        <linearGradient id="steel" x1="0" y1="0" x2="1" y2="1">
          <stop offset="0" stop-color="var(--steel-light)"/>
          <stop offset="0.55" stop-color="var(--steel-mid)"/>
          <stop offset="1" stop-color="var(--steel-dark)"/>
        </linearGradient>
        <radialGradient id="mesh" cx="0.35" cy="0.45" r="0.8">
          <stop offset="0" stop-color="var(--mesh-light)"/>
          <stop offset="1" stop-color="var(--mesh-dark)"/>
        </radialGradient>
        <radialGradient id="photo-flange" cx="0.62" cy="0.35" r="0.75">
          <stop offset="0" stop-color="#efe2cf"/>
          <stop offset="0.35" stop-color="#c7ab8c"/>
          <stop offset="0.7" stop-color="#8a6d55"/>
          <stop offset="1" stop-color="#3f3028"/>
        </radialGradient>
        <radialGradient id="photo-turret" cx="0.6" cy="0.5" r="0.75">
          <stop offset="0" stop-color="#d6dbe2"/>
          <stop offset="0.4" stop-color="#8f9aab"/>
          <stop offset="0.75" stop-color="#4a5366"/>
          <stop offset="1" stop-color="#22262e"/>
        </radialGradient>
      </defs>
      <rect class="steel-plate" width="670" height="518" fill="url(#steel)"/>
      <rect class="mesh-panel" x="330" y="228" width="340" height="178" fill="url(#mesh)" role="img" aria-label="Perforated metal mesh texture"/>
      <path class="band-backing" d="M0 42 H338 L326 420 H0 Z" fill="var(--white)"/>
      <path class="band-stripe-top" d="M0 48 H334 L333 62 H0 Z" fill="var(--orange)"/>
      <path class="band-headline" d="M0 69 H318 V174 H0 Z" fill="var(--orange)"/>
      <path class="band-pitch" d="M0 182 H338 Q346 182 345 190 L328 376 Q327 385 318 385 H0 Z" fill="var(--orange)"/>
      <path class="band-stripe-bottom" d="M0 392 H322 V412 H0 Z" fill="var(--orange)"/>
      <path class="photo-flange" role="img" aria-label="Close-up of a machined steel flange with bolt holes"
            d="M360 24 H670 V230 H290 Q272 230 276 214 L340 38 Q346 24 360 24 Z"
            fill="url(#photo-flange)" stroke="var(--white)" stroke-width="4" stroke-linejoin="round"/>
      <path class="photo-turret" role="img" aria-label="CNC turret punch machine with tool stations and a red emergency stop"
            d="M392 287 H670 V490 H432 Q418 490 416 476 L378 302 Q376 287 392 287 Z"
            fill="url(#photo-turret)" stroke="var(--white)" stroke-width="4" stroke-linejoin="round"/>
    </svg>

    <h1 class="headline headline-lead">WANT TO SELL</h1>
    <p class="headline headline-sub">MACHINE TOOLS &amp;</p>
    <p class="headline headline-small">FABRICATION EQUIPMENT?</p>

    <p class="pitch">
      <span class="pitch-open">We are here</span>
      <span class="pitch-line-1">in your area to pay more</span>
      <span class="pitch-line-2">money on your trade in</span>
      <span class="pitch-line-3">machines than the</span>
      <span class="pitch-line-4">new dealers are</span>
      <span class="pitch-close">offering</span>
    </p>

    <p class="brand-name">T &amp; W EQUIPMENT TRADERS, INC.</p>
  </section>

  <section class="card card-back" aria-label="Postcard back">
    <svg class="card-art" width="674" height="522" viewBox="0 0 674 522">
      <defs>
        <radialGradient id="photo-sparks" cx="0.55" cy="0.6" r="0.7">
          <stop offset="0" stop-color="#ffe9a8"/>
          <stop offset="0.3" stop-color="#d9a54e"/>
          <stop offset="0.65" stop-color="#7a5430"/>
          <stop offset="1" stop-color="#2a201a"/>
        </radialGradient>
      </defs>
      <rect class="side-panel" width="325" height="522" fill="var(--orange)"/>
      <path class="photo-grinding" role="img" aria-label="Worker grinding metal with a shower of sparks"
            d="M0 15 H190 Q205 15 212 28 L255 188 Q258 220 238 220 H0 Z"
            fill="url(#photo-sparks)" stroke="var(--white)" stroke-width="4" stroke-linejoin="round"/>
      <path class="contact-box"
            d="M100 247 H325 V470 H42 Q30 470 33 456 L84 260 Q88 247 100 247 Z"
            fill="var(--charcoal)" stroke="var(--white)" stroke-width="4" stroke-linejoin="round"/>
      <rect class="stamp-box" x="558" y="62" width="74" height="80" fill="none" stroke="var(--ink)" stroke-width="2"/>
      <g class="address-lines" stroke="var(--ink)" stroke-width="2">
        <line x1="368" y1="216" x2="658" y2="216"/>
        <line x1="368" y1="259" x2="658" y2="259"/>
        <line x1="368" y1="305" x2="658" y2="305"/>
      </g>
    </svg>

    <address class="contact">
      <p class="contact-name">T &amp; W Equipment Traders Inc</p>
      <ul class="contact-list">
        <li>(248) 555-0143</li>
        <li>Fax (248) 555-0197</li>
        <li>sales@twequiptraders.example</li>
        <li>www.twequiptraders.example</li>
        <li>www.usedvalmorgrindersandpresses.example</li>
      </ul>
    </address>
  </section>

</main>
</body>
</html>
```